Sandwich board

We are a Photo booth company in NZ.
We need a sandwich board design we have all the guts and we know the style we want just need help making it look good/right.
Dimension of the board are 59cm by 69cm.
The other side is a chalk board so we can write about the event we are at.
The board is a light white wash ply and we will be applying by stencil or dye cut vinyl.
The words are
Just grab a prop
and strike a pose
take your own
black and white or colour
photos
And a carriage with a camera in the back.

Reason: I would like to see a bit more of a play around with the fonts and style.

Target Market(s)

this will be at event mostly weddings, birthdays, fairs really any event.

Industry/Entity Type

Camera

Requirements
Must have
• it must be black with white back ground
Nice to have
• simple lines
Should not have
• colour. to much little detail.

```html
<!DOCTYPE html>
<html lang="en">
<head>
<meta charset="utf-8">
<title>Photo Booth Sandwich Board</title>
<link rel="stylesheet" href="https://fonts.googleapis.com/css2?family=Arvo:wght@400;700&family=Chango&family=Chewy&family=Courier+Prime:wght@700&family=Passion+One:wght@700&family=Ultra&family=Yellowtail&display=swap">
<style>
  :root {
    --ink: #333333;
    --board: #ffffff;
    --art-tone: #8a8a8a;
  }
  * { margin: 0; padding: 0; box-sizing: border-box; }
  html, body {
    width: 1011px;
    height: 1200px;
    overflow: hidden;
    background: var(--board);
  }
  .board {
    position: relative;
    width: 1011px;
    height: 1200px;
    background: var(--board);
    color: var(--ink);
  }
  .board-frame {
    position: absolute;
    inset: 0;
    width: 1011px;
    height: 1200px;
  }
  .line {
    position: absolute;
    left: 0;
    width: 1011px;
    text-align: center;
    white-space: nowrap;
    line-height: 1;
  }
  .just {
    top: 86px;
    left: -50px;
    font-family: "Chewy", cursive;
    font-size: 50px;
    letter-spacing: 3px;
    color: var(--board);
    -webkit-text-stroke: 2.5px var(--ink);
  }
  .grab-a-prop {
    top: 140px;
    left: -50px;
    font-family: "Passion One", sans-serif;
    font-weight: 700;
    font-size: 86px;
    letter-spacing: 1px;
  }
  .strike-a {
    top: 222px;
    left: -60px;
    font-family: "Yellowtail", cursive;
    font-size: 100px;
  }
  .pose {
    top: 328px;
    left: -52px;
    font-family: "Ultra", serif;
    font-size: 98px;
  }
  .divider {
    position: absolute;
    top: 440px;
    left: 168px;
    width: 596px;
    height: 18px;
  }
  .take-your-own {
    top: 466px;
    left: -56px;
    font-family: "Courier Prime", monospace;
    font-weight: 700;
    font-size: 24px;
    letter-spacing: 2px;
  }
  .choice {
    position: absolute;
    top: 500px;
    left: 160px;
    width: 700px;
    height: 100px;
    font-family: "Arvo", serif;
  }
  .choice-word {
    position: absolute;
    font-size: 62px;
    line-height: 1;
  }
  .choice-black { left: 0; top: 0; }
  .choice-white { left: 192px; top: 36px; }
  .choice-colour { left: 432px; top: 34px; }
  .choice-joiner {
    position: absolute;
    font-size: 20px;
    line-height: 1;
    padding: 1px 3px;
    background: var(--ink);
    color: var(--board);
  }
  .choice-and { left: 200px; top: 10px; }
  .choice-or { left: 405px; top: 28px; }
  .photos {
    top: 598px;
    left: -16px;
    font-family: "Chango", sans-serif;
    font-size: 100px;
    letter-spacing: 2px;
  }
  .carriage-art {
    position: absolute;
    left: 257px;
    top: 718px;
    width: 520px;
    height: 396px;
    background: radial-gradient(ellipse at 50% 55%, var(--art-tone) 0%, #c8c8c8 60%, var(--board) 100%);
  }
</style>
</head>
<body>
<main class="board">
  <svg class="board-frame" viewBox="0 0 1011 1200" aria-hidden="true">
    <path fill="#333333" fill-rule="evenodd" d="
      M0 0 H1011 V1200 H0 Z
      M22 28
      L120 20 L180 34 L260 18 L360 30 L470 16 L560 32 L650 20 L760 34 L850 18 L940 30 L985 26
      L975 120 L990 210 L968 300 L982 420 L962 520 L980 640 L958 760 L976 880 L960 980 L978 1080 L966 1160
      L880 1170 L790 1156 L690 1174 L590 1158 L480 1176 L380 1160 L270 1172 L170 1156 L70 1170 L28 1164
      L40 1080 L20 980 L42 880 L24 760 L46 640 L26 520 L44 400 L22 300 L40 200 L20 110 Z"/>
  </svg>

  <p class="line just">JUST</p>
  <p class="line grab-a-prop">GRAB A PROP</p>
  <p class="line strike-a">&amp; Strike a</p>
  <p class="line pose">POSE!</p>

  <svg class="divider" viewBox="0 0 596 18" aria-hidden="true">
    <line x1="12" y1="9" x2="584" y2="9" stroke="#333333" stroke-width="3"/>
    <path d="M0 9 L12 3 L12 15 Z" fill="#333333"/>
    <path d="M596 9 L584 3 L584 15 Z" fill="#333333"/>
    <circle cx="26" cy="9" r="4" fill="none" stroke="#333333" stroke-width="2"/>
    <circle cx="570" cy="9" r="4" fill="none" stroke="#333333" stroke-width="2"/>
  </svg>

  <p class="line take-your-own">TAKE YOUR OWN</p>

  <div class="choice">
    <span class="choice-word choice-black">Black</span>
    <span class="choice-joiner choice-and">And</span>
    <span class="choice-word choice-white">White</span>
    <span class="choice-joiner choice-or">Or</span>
    <span class="choice-word choice-colour">Colour</span>
  </div>

  <p class="line photos">PHOTOS</p>

  <div class="carriage-art" role="img" aria-label="Vintage horse-drawn carriage with a large bellows camera mounted on the back and a driver holding a whip"></div>
</main>
</body>
</html>
```